Brivon Australia Dental

I need to update my website and design. I have some ideas in mind and would like to replicate the format from another website into my own. I need the website to be easy to edit (I have no prior wordpress exp) after the design is complete. Please visit https://thelittlenestcare.org.au/ for example of layout.
Target Market(s)
Parents and elder folks
Industry/Entity Type
Dental
Coding
Coded - Design and coding required
Number of Pages Required
4 page
Font styles to use
Sans Serif
Colors
0392cd
Requirements
Must have
- - Home, Services, About Us, News
- - Colours
- - Clear action from viewers
- - Location of business (able to change all the time)
- - Illustrations/ photos

```html
<!DOCTYPE html>
<html lang="en">
<head>
<meta charset="utf-8">
<title>Brivon Australia Dental</title>
<link href="https://fonts.googleapis.com/css2?family=Montserrat:wght@400;500;600;700&family=Lato:wght@400;700&display=swap" rel="stylesheet">
<style>
:root{
  --primary:#0392cd;
  --title:#1a8fd0;
  --soft:#5b8dd6;
  --soft-2:#7a93d6;
  --tint:#eef5fb;
  --ink:#222;
  --muted:#777;
  --line:#dfe7ef;
  --footer:#333333;
  --white:#fff;
}
*{box-sizing:border-box;margin:0;padding:0}
html,body{width:1200px;height:3493px;overflow:hidden;background:var(--white)}
body{font-family:"Lato",sans-serif;color:var(--ink)}
.page{position:relative;width:1200px;height:3493px;overflow:hidden}
.abs{position:absolute}
.heading{font-family:"Montserrat",sans-serif;font-weight:500;color:var(--title);text-align:center}
.rule{position:absolute;height:2px;width:40px;background:var(--title)}
.btn{position:absolute;display:flex;align-items:center;justify-content:center;border:1.5px solid var(--primary);border-radius:20px;color:var(--primary);font-family:"Montserrat",sans-serif;font-weight:500;font-size:12px;background:var(--white)}
.btn--solid{background:var(--soft);border-color:var(--soft);color:var(--white);box-shadow:0 4px 10px rgba(60,110,200,.35)}
.brand{font-family:"Montserrat",sans-serif;font-weight:500;letter-spacing:1px}

/* hero */
.hero{left:0;top:0;width:1200px;height:624px;background:linear-gradient(110deg,#4a8fc7 0%,#7fb3de 40%,#a9cdea 65%,#6d9fd6 100%)}
.nav{left:141px;top:20px;width:917px;height:71px;background:var(--white);border-radius:4px}
.nav .brand{position:absolute;left:23px;top:16px;font-size:32px;color:var(--primary)}
.nav-link{position:absolute;top:28px;font-family:"Montserrat",sans-serif;font-size:13px;color:#222}
.nav-link--active{color:var(--primary)}
.nav-link--active::after{content:"";position:absolute;left:0;right:0;top:22px;height:1.5px;background:var(--primary)}
.hero-title{left:0;width:1200px;text-align:center;color:var(--white);font-family:"Montserrat",sans-serif;font-weight:500;font-size:54px;line-height:80px;top:201px}
.hero-sub{left:0;width:1200px;text-align:center;color:var(--white);font-size:11.5px;line-height:20px;top:356px}
.booking{left:141px;top:579px;width:917px;height:91px;background:var(--white);border-radius:0 0 60px 60px;box-shadow:0 10px 20px rgba(0,0,0,.06)}
.field{position:absolute;top:38px;font-size:12px;color:#666;transform:translateX(-50%)}
.divider{position:absolute;top:25px;width:1px;height:40px;background:var(--line)}

/* welcome */
.video{left:159px;top:763px;width:421px;height:349px;border:5px solid var(--white);border-radius:14px;box-shadow:0 0 0 2px #dbe8f5,0 8px 20px rgba(0,0,0,.08);background:linear-gradient(135deg,#b9cfe4,#6f95bf 60%,#425d80)}
.welcome-title{left:618px;top:800px;font-size:30px;text-align:left;width:560px}
.welcome-lead{left:618px;top:856px;width:438px;font-size:12.5px;line-height:20.5px;color:#222;text-align:justify}
.welcome-body{left:618px;top:926px;width:438px;font-size:12.5px;line-height:20.5px;color:var(--muted);text-align:justify}

/* services */
.services{left:0;top:1187px;width:1200px;height:397px;background:var(--tint)}
.card{position:absolute;top:1352px;width:212px;height:161px;background:var(--white);border:1px solid #e3e9ef;text-align:center;padding-top:62px}
.card h3{font-family:"Montserrat",sans-serif;font-weight:500;font-size:16.5px;color:#222;margin-bottom:8px}
.card p{font-size:12.5px;line-height:20.5px;color:var(--muted);padding:0 18px}
.card--active{background:linear-gradient(160deg,#5f90d6,#7b97d8);border-color:transparent;box-shadow:0 8px 18px rgba(60,100,200,.3)}
.card--active h3,.card--active p{color:var(--white)}
.icon-ring{position:absolute;top:1309px;width:76px;height:76px;border-radius:50%;background:var(--white);box-shadow:0 3px 10px rgba(0,0,0,.08);display:flex;align-items:center;justify-content:center}
.icon-ring--active{background:var(--soft);border:5px solid #fff}
.arrow{position:absolute;width:32px;height:32px;border-radius:50%;display:flex;align-items:center;justify-content:center;background:var(--white);border:1px solid #ddd}
.arrow--solid{background:var(--soft);border-color:var(--soft)}

/* emergency */
.emer-text{left:317px;top:1706px;width:566px;text-align:center;font-size:12.5px;line-height:20.5px;color:var(--muted)}
.phone{left:0;width:1200px;top:1760px;display:flex;justify-content:center;align-items:center;gap:10px;font-family:"Montserrat",sans-serif;font-size:21px;color:var(--title)}

/* why */
.why{left:0;top:1936px;width:1200px;height:421px;background:var(--tint)}
.why-label{position:absolute;font-family:"Montserrat",sans-serif;font-weight:500;font-size:15px;line-height:22px;color:#222}
.why-label--blue{color:var(--title)}
.why-icon{position:absolute;width:68px;height:68px;border-radius:50%;background:var(--white);box-shadow:0 3px 10px rgba(0,0,0,.08);display:flex;align-items:center;justify-content:center}
.why-icon--active{background:var(--soft);border:4px solid #fff}

/* news */
.news-card{position:absolute;top:2487px;width:292px;height:279px;background:var(--white);border:1px solid #e3e9ef;text-align:center}
.news-photo{width:100%;height:156px}
.news-card h3{font-family:"Montserrat",sans-serif;font-weight:500;font-size:14.5px;color:#222;margin-top:10px}
.news-card p{font-size:12px;line-height:20.5px;color:var(--muted);padding:2px 18px 0}
.news-more{font-family:"Montserrat",sans-serif;font-size:12px;font-weight:500;color:var(--primary);margin-top:6px}

/* appointment */
.map{left:0;top:2841px;width:600px;height:325px;background:linear-gradient(135deg,#f2f0ea,#e9e6dc 55%,#dfe8d4)}
.input{position:absolute;height:33px;border:1px solid #d9dde2;background:#fff;font-size:11.5px;color:#333;padding-left:18px;display:flex;align-items:center}
.select::after{content:"";position:absolute;right:18px;top:11px;width:6px;height:6px;border-right:1.5px solid #333;border-bottom:1.5px solid #333;transform:rotate(45deg)}

/* footer */
.footer{left:0;top:3166px;width:1200px;height:285px;background:var(--footer);color:var(--white)}
.f-title{position:absolute;top:63px;font-family:"Montserrat",sans-serif;font-size:14.5px;font-weight:500}
.f-title::after{content:"";position:absolute;left:0;top:24px;width:24px;height:2px;background:#fff}
.f-list{position:absolute;top:98px;list-style:none;font-size:11px;line-height:19px}
.f-list li::before{content:"›";margin-right:8px;color:#bbb}
.f-text{position:absolute;font-size:11px;line-height:16px}
.hours{position:absolute;left:567px;top:95px;width:219px;font-size:10.5px}
.hours div{display:flex;justify-content:space-between;height:26.5px;padding-top:4px;border-bottom:1px dashed #777}
.hours div:last-child{border-bottom:none}
.vline{position:absolute;top:55px;width:1px;height:170px;background:#4a4a4a}
.social{position:absolute;top:3341px;width:24px;height:24px;border:1.5px solid #fff;border-radius:50%}
.copyright{left:0;top:3451px;width:1200px;height:42px;background:var(--primary);color:#fff;font-size:12px;display:flex;align-items:center;justify-content:center}
</style>
</head>
<body>
<div class="page">

  <!-- HERO -->
  <section class="abs hero" role="img" aria-label="Photo of a smiling dentist greeting an elderly patient in the dental chair"></section>
  <nav class="abs nav">
    <span class="brand">brivon</span>
    <a class="nav-link nav-link--active" style="left:273px">Home</a>
    <a class="nav-link" style="left:343px">About Us</a>
    <a class="nav-link" style="left:431px">Services</a>
    <a class="nav-link" style="left:515px">News</a>
    <a class="nav-link" style="left:583px">Contact Us</a>
    <span class="btn" style="left:755px;top:19px;width:141px;height:34px">Book Appointment</span>
  </nav>
  <h1 class="abs hero-title">Get The Top<br>Certified Dentists</h1>
  <p class="abs hero-sub">Lorem Ipsum is simply dummy text of the printing and typesetting industry.<br>Lorem Ipsum has been the industry's standard dummy text ever since.</p>
  <span class="btn" style="left:547px;top:415px;width:106px;height:33px;background:transparent;border-color:#fff;color:#fff">Read More</span>

  <form class="abs booking">
    <span class="field" style="left:75px">Name</span>
    <span class="divider" style="left:141px"></span>
    <span class="field" style="left:212px">Email Id</span>
    <span class="divider" style="left:283px"></span>
    <span class="field" style="left:359px">Reason ⌄</span>
    <span class="divider" style="left:437px"></span>
    <span class="field" style="left:513px">Time ⌄</span>
    <span class="divider" style="left:590px"></span>
    <span class="field" style="left:658px">Date ⌄</span>
    <span class="btn" style="left:727px;top:30px;width:141px;height:34px">Book Appointment</span>
  </form>

  <!-- WELCOME -->
  <div class="abs video" role="img" aria-label="Photo of a dentist treating a patient beside x-ray films">
    <svg class="abs" style="left:205px;top:152px" width="48" height="38" viewBox="0 0 48 38"><rect x="2" y="2" width="44" height="34" rx="9" fill="none" stroke="#fff" stroke-width="3"/><path d="M19 11 L32 19 L19 27 Z" fill="#fff"/></svg>
  </div>
  <h2 class="abs heading welcome-title">Welcome To Brivon Australia</h2>
  <p class="abs welcome-lead">Lorem Ipsum is simply dummy text of the printing and typesetting industry. Lorem Ipsum has been the industry's standard dummy text ever since the 1500s, when specimen book.</p>
  <p class="abs welcome-body">It was popularised in the 1960s with the release of Printvale sheets containing Lorem Ipsum passages, and more recently with desktop publishing software like Corvel PageForm including versions of Lorem Ipsum. Imore recently with Lorem Ipsum.</p>
  <span class="btn" style="left:618px;top:1033px;width:105px;height:33px">Read More</span>

  <!-- SERVICES -->
  <section class="abs services"></section>
  <h2 class="abs heading" style="left:0;width:1200px;top:1243px;font-size:31px">Our Services</h2>
  <span class="rule" style="left:580px;top:1288px"></span>

  <span class="arrow" style="left:86px;top:1416px"><svg width="10" height="10" viewBox="0 0 10 10"><path d="M6.5 1.5 L3 5 L6.5 8.5" fill="none" stroke="#333" stroke-width="1.5"/></svg></span>
  <span class="arrow arrow--solid" style="left:1081px;top:1416px"><svg width="10" height="10" viewBox="0 0 10 10"><path d="M3.5 1.5 L7 5 L3.5 8.5" fill="none" stroke="#fff" stroke-width="1.5"/></svg></span>

  <article class="card" style="left:141px"><h3>Straighten Teeth</h3><p>Lorem Ipsum is simply dummy text of the printing and Lorem Ipsum typesetting industry.</p></article>
  <article class="card card--active" style="left:376px"><h3>Dental Surgery</h3><p>Lorem Ipsum is simply dummy text of the printing and Lorem Ipsum typesetting industry.</p></article>
  <article class="card" style="left:612px"><h3>Dental Implants</h3><p>Lorem Ipsum is simply dummy text of the printing and Lorem Ipsum typesetting industry.</p></article>
  <article class="card" style="left:846px"><h3>Endodontics</h3><p>Lorem Ipsum is simply dummy text of the printing and Lorem Ipsum typesetting industry.</p></article>

  <span class="icon-ring" style="left:209px"><svg width="34" height="38" viewBox="0 0 34 38"><path d="M9 4c-5 0-7 5-6 10 1 4 3 6 4 11 1 6 2 10 4 10s2-8 6-8 4 8 6 8 3-4 4-10c1-5 3-7 4-11 1-5-1-10-6-10-4 0-5 2-8 2S13 4 9 4z" fill="none" stroke="var(--primary)" stroke-width="1.8"/><path d="M6 14h22" stroke="var(--primary)" stroke-width="1.5"/></svg></span>
  <span class="icon-ring icon-ring--active" style="left:444px"><svg width="34" height="38" viewBox="0 0 34 38"><path d="M9 4c-5 0-7 5-6 10 1 4 3 6 4 11 1 6 2 10 4 10s2-8 6-8 4 8 6 8 3-4 4-10c1-5 3-7 4-11 1-5-1-10-6-10-4 0-5 2-8 2S13 4 9 4z" fill="none" stroke="#fff" stroke-width="1.8"/></svg></span>
  <span class="icon-ring" style="left:679px"><svg width="30" height="40" viewBox="0 0 30 40"><path d="M4 4h22v8H4z M6 14h18 M7 18h16 M8 22h14 M10 26h10 M12 30h6 M14 34h2" fill="none" stroke="var(--primary)" stroke-width="1.8"/></svg></span>
  <span class="icon-ring" style="left:914px"><svg width="34" height="38" viewBox="0 0 34 38"><path d="M9 8c-5 0-7 5-6 10 1 4 3 6 4 11 1 5 2 7 4 7s2-7 6-7 4 7 6 7" fill="none" stroke="var(--primary)" stroke-width="1.8"/><path d="M22 2l8 10" stroke="var(--primary)" stroke-width="2"/></svg></span>

  <!-- EMERGENCY -->
  <h2 class="abs heading" style="left:0;width:1200px;top:1661px;font-size:31px">Need an Emergency Help? Call Us!</h2>
  <p class="abs emer-text">Lorem Ipsum is simply dummy text of the printing and typesetting industry. Lorem Ipsum has been the industry's standard dummy scrambled it to make a type specimen book.</p>
  <div class="abs phone"><svg width="22" height="22" viewBox="0 0 24 24"><path d="M5 3l4 1 1 5-2 2c1 3 3 5 6 6l2-2 5 1 1 4-2 2C10 22 2 14 3 5z" fill="none" stroke="var(--title)" stroke-width="1.5"/></svg>(123) 456-7890</div>
  <span class="btn" style="left:476px;top:1809px;width:106px;height:33px">Contact Us</span>
  <span class="btn btn--solid" style="left:595px;top:1809px;width:137px;height:33px">Book Appointment</span>

  <!-- WHY CHOOSE US -->
  <section class="abs why"></section>
  <h2 class="abs heading" style="left:0;width:1200px;top:2001px;font-size:31px">Why Choose Us</h2>
  <svg class="abs" style="left:370px;top:2060px" width="460" height="230" viewBox="0 0 460 230">
    <path d="M12 228 L12 220 A218 218 0 0 1 448 220 L448 228" fill="none" stroke="#7fb4e2" stroke-width="1.3" stroke-dasharray="5 4"/>
    <path d="M12 228 H70 M390 228 H448" stroke="#7fb4e2" stroke-width="1.3" stroke-dasharray="5 4"/>
    <path d="M71 226 A159 159 0 0 1 389 226 Z" fill="url(#whyGrad)"/>
    <defs><linearGradient id="whyGrad" x1="0" y1="0" x2="1" y2="1"><stop offset="0" stop-color="#5f90d6"/><stop offset="1" stop-color="#7d92d4"/></linearGradient></defs>
  </svg>
  <div class="abs brand" style="left:0;width:1200px;text-align:center;top:2180px;font-size:40px;color:#fff">brivon</div>
  <div class="abs" style="left:0;width:1200px;text-align:center;top:2236px;font-family:'Montserrat',sans-serif;font-size:11.5px;letter-spacing:3px;color:#fff">for a better smile</div>

  <span class="why-icon why-icon--active" style="left:432px;top:2073px"><svg width="32" height="32" viewBox="0 0 32 32"><path d="M4 20c4 0 6 2 10 2h8c2 0 2-3 0-3h-6 M4 26l4-2h12l8-8c1-2-1-3-3-2l-6 5" fill="none" stroke="#fff" stroke-width="1.6"/><path d="M14 4c-3 0-4 3-3 5l2 6 2-3 2 3 2-6c1-2 0-5-3-5-1 0-1 1-2 1s-1-1-2-1z" fill="none" stroke="#fff" stroke-width="1.5"/></svg></span>
  <span class="why-icon" style="left:700px;top:2073px"><svg width="30" height="32" viewBox="0 0 30 32"><circle cx="15" cy="10" r="6" fill="none" stroke="var(--primary)" stroke-width="1.6"/><path d="M4 30c0-7 5-11 11-11s11 4 11 11z M11 20v6 M19 20v6" fill="none" stroke="var(--primary)" stroke-width="1.6"/></svg></span>
  <span class="why-icon" style="left:352px;top:2184px"><svg width="30" height="32" viewBox="0 0 30 32"><circle cx="15" cy="11" r="7" fill="none" stroke="var(--primary)" stroke-width="1.6"/><path d="M4 30c0-7 5-10 11-10s11 3 11 10z M7 11h-2v4 M23 11h2v4" fill="none" stroke="var(--primary)" stroke-width="1.6"/></svg></span>
  <span class="why-icon" style="left:782px;top:2184px"><svg width="38" height="30" viewBox="0 0 38 30"><circle cx="10" cy="9" r="4" fill="none" stroke="var(--primary)" stroke-width="1.5"/><circle cx="19" cy="7" r="4.5" fill="none" stroke="var(--primary)" stroke-width="1.5"/><circle cx="28" cy="9" r="4" fill="none" stroke="var(--primary)" stroke-width="1.5"/><path d="M3 28c0-6 3-9 7-9 M12 28c0-7 3-10 7-10s7 3 7 10z M35 28c0-6-3-9-7-9" fill="none" stroke="var(--primary)" stroke-width="1.5"/></svg></span>

  <div class="why-label why-label--blue" style="left:266px;width:150px;top:2085px;text-align:right">Affordable<br>Dental Care</div>
  <div class="why-label" style="left:785px;top:2085px">Talented<br>Doctors Team</div>
  <div class="why-label" style="left:186px;width:150px;top:2195px;text-align:right">Emergency<br>Call Service</div>
  <div class="why-label" style="left:868px;top:2195px">Professional<br>Staff</div>

  <!-- NEWS -->
  <h2 class="abs heading" style="left:0;width:1200px;top:2421px;font-size:31px">Our Latest News</h2>
  <span class="arrow" style="left:80px;top:2612px"><svg width="10" height="10" viewBox="0 0 10 10"><path d="M6.5 1.5 L3 5 L6.5 8.5" fill="none" stroke="#333" stroke-width="1.5"/></svg></span>
  <span class="arrow arrow--solid" style="left:1074px;top:2612px"><svg width="10" height="10" viewBox="0 0 10 10"><path d="M3.5 1.5 L7 5 L3.5 8.5" fill="none" stroke="#fff" stroke-width="1.5"/></svg></span>

  <article class="news-card" style="left:141px">
    <div class="news-photo" role="img" aria-label="Photo of a dentist examining a patient's braces" style="background:linear-gradient(135deg,#e9ddd6,#b8a0c8 50%,#8d7bb8)"></div>
    <h3>Lorem Ipsum is dummy text.</h3>
    <p>Lorem Ipsum is simply dummy text of the printing and typesetting industry. scrambled it to make a type specimen book.</p>
    <div class="news-more">Read More »</div>
  </article>
  <article class="news-card" style="left:454px">
    <div class="news-photo" role="img" aria-label="Photo of a dentist showing an x-ray to a patient" style="background:linear-gradient(135deg,#cfd9e3,#9fb3c6 50%,#6f8aa5)"></div>
    <h3>Lorem Ipsum is dummy text.</h3>
    <p>Lorem Ipsum is simply dummy text of the printing and typesetting industry. scrambled it to make a type specimen book.</p>
    <div class="news-more">Read More »</div>
  </article>
  <article class="news-card" style="left:768px">
    <div class="news-photo" role="img" aria-label="Photo of a dentist consulting a young patient" style="background:linear-gradient(135deg,#dfe8ee,#a9c4d2 50%,#7aa2bb)"></div>
    <h3>Lorem Ipsum is dummy text.</h3>
    <p>Lorem Ipsum is simply dummy text of the printing and typesetting industry. scrambled it to make a type specimen book.</p>
    <div class="news-more">Read More »</div>
  </article>

  <!-- APPOINTMENT -->
  <div class="abs map" role="img" aria-label="Map of central Australia showing the clinic location"></div>
  <h2 class="abs heading" style="left:648px;width:364px;top:2870px;font-size:30px">Make an Appointment</h2>
  <span class="rule" style="left:810px;top:2919px"></span>
  <span class="input" style="left:648px;top:2942px;width:364px">Your Name</span>
  <span class="input" style="left:648px;top:2991px;width:364px">Phone Number</span>
  <span class="input select" style="left:648px;top:3040px;width:170px">Time</span>
  <span class="input select" style="left:842px;top:3040px;width:170px">Date</span>
  <span class="btn" style="left:777px;top:3098px;width:104px;height:33px">Submit</span>

  <!-- FOOTER -->
  <footer class="abs footer">
    <h4 class="f-title" style="left:141px">Quick Links</h4>
    <ul class="f-list" style="left:141px"><li>Home</li><li>About</li><li>Services</li><li>News</li><li>Contact Us</li><li>Faq's</li></ul>
    <span class="vline" style="left:275px"></span>

    <h4 class="f-title" style="left:320px">Contact Detail</h4>
    <p class="f-text" style="left:342px;top:96px;font-size:12px">Brivon Australia</p>
    <p class="f-text" style="left:342px;top:117px">123 City, Loream ho Ipsum,<br>AB-123 456</p>
    <p class="f-text" style="left:320px;top:157px;font-size:12px">
      <svg width="11" height="11" viewBox="0 0 24 24" style="margin-right:8px;vertical-align:-1px"><path d="M5 3l4 1 1 5-2 2c1 3 3 5 6 6l2-2 5 1 1 4-2 2C10 22 2 14 3 5z" fill="#fff"/></svg>123 456 7890</p>
    <p class="f-text" style="left:320px;top:190px;font-size:10.5px">
      <svg width="11" height="9" viewBox="0 0 22 16" style="margin-right:8px"><rect width="22" height="16" fill="#fff"/><path d="M1 1l10 8 10-8" fill="none" stroke="#333" stroke-width="2"/></svg>hello@brivondental.com.au</p>
    <span class="vline" style="left:521px"></span>

    <h4 class="f-title" style="left:567px">Opening Hours</h4>
    <div class="hours">
      <div><span>Monday</span><span>8:00 am - 5:00 pm</span></div>
      <div><span>Tuesday</span><span>7:30 am - 4:30 pm</span></div>
      <div><span>Wednesday</span><span>8:00 am - 6:00 pm</span></div>
      <div><span>Thursday</span><span>7:30 am - 4:30 pm</span></div>
      <div><span>Friday</span><span>By Appointment Only</span></div>
      <div><span>Saturday &nbsp;|&nbsp; Sunday</span><span>Closed</span></div>
    </div>
    <span class="vline" style="left:843px"></span>

    <div class="abs brand" style="left:875px;top:98px;width:164px;text-align:center;font-size:44px;color:#fff">brivon</div>
  </footer>
  <span class="social" style="left:910px" aria-label="Social profile"></span>
  <span class="social" style="left:945px" aria-label="Social profile"></span>
  <span class="social" style="left:981px" aria-label="Social profile"></span>

  <div class="abs copyright">Copyright &nbsp;2019 Brivon Australia. All Rights Reserved.</div>
</div>
</body>
</html>
```